Business cards

I would like a black background with the design I previously chose. I need 2 sets of cards. Mine will have Marisol Brandt, Broker/Owner, 307-555-0148 and marisol.harborpeak@mailvista.com
The second set will read, Dana Rutledge, Realtor 307-555-0172, dana.harborpeak@mailvista.com

Industry/Entity Type

Business

```html
<!DOCTYPE html>
<html lang="en">
<head>
<meta charset="UTF-8">
<title>Dana Rutledge – Business Card</title>
<link href="https://fonts.googleapis.com/css2?family=Arimo:wght@700&display=swap" rel="stylesheet">
<style>
  :root {
    --card-black: #000000;
    --smoke-dark: #151515;
    --smoke-light: #262626;
    --swoosh-deep: #1f5f10;
    --swoosh-bright: #9fd41c;
    --text-light: #f8eef1;
    --text-white: #ffffff;
  }
  html, body {
    margin: 0;
    padding: 0;
    width: 1200px;
    height: 686px;
    overflow: hidden;
    background: var(--card-black);
  }
  .business-card {
    position: relative;
    width: 1200px;
    height: 686px;
    overflow: hidden;
    font-family: "Arimo", Arial, sans-serif;
    font-weight: 700;
  }
  .card-art {
    position: absolute;
    inset: 0;
    width: 1200px;
    height: 686px;
  }
  .contact {
    position: absolute;
    left: 0;
    top: 0;
    margin: 0;
    line-height: 1;
    white-space: nowrap;
  }
  .contact-name {
    left: 45px;
    top: 202px;
    font-size: 62px;
    color: var(--text-light);
  }
  .contact-title {
    left: 186px;
    top: 305px;
    font-size: 41px;
    color: var(--text-white);
  }
  .contact-phone {
    left: 189px;
    top: 396px;
    font-size: 43px;
    color: var(--text-white);
  }
  .contact-email {
    left: 57px;
    top: 488px;
    font-size: 45px;
    color: var(--text-white);
  }
</style>
</head>
<body>
  <main class="business-card">
    <svg class="card-art" viewBox="0 0 1200 686" xmlns="http://www.w3.org/2000/svg" aria-hidden="true">
      <defs>
        <radialGradient id="smokeTone" cx="0.75" cy="0.2" r="0.8">
          <stop offset="0" stop-color="var(--smoke-light)"/>
          <stop offset="1" stop-color="var(--smoke-dark)"/>
        </radialGradient>
        <linearGradient id="swooshTone" x1="0" y1="0" x2="1" y2="0.6">
          <stop offset="0" stop-color="var(--swoosh-bright)"/>
          <stop offset="0.45" stop-color="var(--swoosh-deep)"/>
          <stop offset="0.8" stop-color="var(--swoosh-bright)"/>
          <stop offset="1" stop-color="var(--swoosh-bright)"/>
        </linearGradient>
      </defs>
      <rect class="smoke-field" width="1200" height="686" fill="url(#smokeTone)" role="img" aria-label="Faint dark smoke texture"/>
      <path class="swoosh" fill="url(#swooshTone)"
            d="M0,0 C420,70 930,205 1125,385 C1235,488 1215,610 1030,686 L0,686 Z"/>
      <path class="black-panel" fill="var(--card-black)"
            d="M0,9 C400,88 900,228 1098,400 C1200,490 1185,600 1006,686 L0,686 Z"/>
    </svg>

    <h1 class="contact contact-name">Dana Rutledge</h1>
    <p class="contact contact-title">Realtor</p>
    <p class="contact contact-phone">307-555-0172</p>
    <p class="contact contact-email">dana.harborpeak@mailvista.com</p>
  </main>
</body>
</html>
```